Footpath/Sidewalk inspection company needs poster

We need a poster for an upcoming technical conference. Our company has a specialist footpath/sidewalk inspection system. The poster is to be mounted on the outside of our booth to get the interest of potential customers.
I would like the main part of the poster to have the image "P3060103" but transparent or faded. The large main text should say "Do you need to know where every individual fault is on your footpath network?"
A smaller part of the poster should have the map "Zoom Out" with an expanding view to the "Zoom in" image. This part should have small text "Whakatane District, 15,700 faults recorded"
Road Engineers
It Company

```html
<!DOCTYPE html>
<html lang="en">
<head>
<meta charset="utf-8">
<title>Footpath Network Banner</title>
<link rel="stylesheet" href="https://fonts.googleapis.com/css2?family=Source+Sans+3:wght@400;600&display=swap">
<style>
  :root {
    --page-bg: #2b2b2d;
    --banner-white: #f1f1f3;
    --navy-text: #1d2a6e;
    --blue-deep: #1c3388;
    --blue-mid: #2a47a6;
    --blue-soft: #4b5fb8;
    --grey-band: #5b5c61;
    --grey-light: #8e8f95;
    --accent-orange: #d2552a;
    --logo-ink: #2a2a2e;
  }
  * { box-sizing: border-box; margin: 0; padding: 0; }
  html, body { width: 1200px; height: 900px; overflow: hidden; }
  body {
    background: var(--page-bg);
    font-family: "Source Sans 3", "Myriad Pro", sans-serif;
  }
  .banner {
    position: absolute;
    left: 415px;
    top: 15px;
    width: 370px;
    height: 870px;
    background: var(--banner-white);
    overflow: hidden;
    box-shadow: 0 6px 24px rgba(0,0,0,0.45);
  }
  .banner-shapes, .street-photo, .map-circles {
    position: absolute;
    left: 0; top: 0;
    width: 370px; height: 870px;
  }
  .headline {
    position: absolute;
    top: 14px; left: 0; right: 0;
    text-align: center;
    color: var(--navy-text);
    font-size: 22.5px;
    font-weight: 400;
    line-height: 28px;
  }
  .caption {
    position: absolute;
    top: 668px; left: 0; right: 0;
    text-align: center;
    color: #ffffff;
    font-size: 15px;
    line-height: 20px;
  }
  .brand {
    position: absolute;
    right: 26px;
    bottom: 14px;
    text-align: right;
  }
  .brand-name {
    display: flex;
    align-items: center;
    justify-content: flex-end;
    gap: 8px;
    color: var(--logo-ink);
    font-size: 22px;
    font-weight: 600;
    line-height: 26px;
  }
  .brand-dot {
    width: 14px; height: 14px;
    border-radius: 50%;
    background: var(--accent-orange);
  }
  .brand-web {
    color: var(--accent-orange);
    font-size: 8.5px;
    margin-top: 3px;
  }
</style>
</head>
<body>
  <main class="banner">
    <svg class="banner-shapes" viewBox="0 0 370 870" aria-hidden="true">
      <defs>
        <linearGradient id="blueField" x1="0" y1="0" x2="1" y2="1">
          <stop offset="0" stop-color="var(--blue-deep)"/>
          <stop offset="0.6" stop-color="var(--blue-mid)"/>
          <stop offset="1" stop-color="var(--blue-deep)"/>
        </linearGradient>
        <linearGradient id="greyBand" x1="0" y1="0" x2="1" y2="0">
          <stop offset="0" stop-color="#4c4d52"/>
          <stop offset="1" stop-color="#7a7b80"/>
        </linearGradient>
      </defs>
      <polygon points="0,178 370,93 370,128 0,216" fill="url(#greyBand)"/>
      <polygon points="0,548 370,420 370,870 0,870" fill="url(#blueField)"/>
      <polygon points="0,520 370,370 370,432 0,552" fill="url(#greyBand)"/>
      <polygon points="0,728 370,712 370,735 0,790" fill="var(--blue-soft)" opacity="0.8"/>
      <polygon points="0,760 220,800 0,840" fill="var(--grey-light)"/>
      <polygon points="0,840 370,742 370,870 0,870" fill="var(--banner-white)"/>
    </svg>

    <svg class="street-photo" viewBox="0 0 370 870" role="img" aria-label="Photograph of a worn footpath beside a kerb and road, with a hedge and grass verge">
      <defs>
        <linearGradient id="photoTone" x1="0" y1="0" x2="1" y2="0.4">
          <stop offset="0" stop-color="#6e7277"/>
          <stop offset="0.45" stop-color="#8a8078"/>
          <stop offset="0.75" stop-color="#7d6a58"/>
          <stop offset="1" stop-color="#4f7a36"/>
        </linearGradient>
      </defs>
      <polygon points="0,190 370,102 370,372 0,522" fill="url(#photoTone)"/>
    </svg>

    <svg class="map-circles" viewBox="0 0 370 870">
      <defs>
        <radialGradient id="mapWide" cx="0.4" cy="0.5" r="0.7">
          <stop offset="0" stop-color="#4d6b3c"/>
          <stop offset="0.7" stop-color="#3d5a36"/>
          <stop offset="1" stop-color="#2f5e86"/>
        </radialGradient>
        <radialGradient id="mapClose" cx="0.5" cy="0.5" r="0.7">
          <stop offset="0" stop-color="#8b8c86"/>
          <stop offset="1" stop-color="#5c6457"/>
        </radialGradient>
      </defs>
      <ellipse cx="105" cy="648" rx="62" ry="6" fill="#000" opacity="0.25"/>
      <ellipse cx="265" cy="648" rx="62" ry="6" fill="#000" opacity="0.25"/>
      <g role="img" aria-label="Zoomed-out aerial map of the district coastline">
        <circle cx="105" cy="570" r="70" fill="url(#mapWide)" stroke="#e9eaee" stroke-width="5"/>
      </g>
      <g role="img" aria-label="Zoomed-in aerial map of town streets">
        <circle cx="265" cy="570" r="70" fill="url(#mapClose)" stroke="#e9eaee" stroke-width="5"/>
      </g>
    </svg>

    <h1 class="headline">Do you need to know where<br>every individual fault is on your<br>FOOTPATH NETWORK?</h1>

    <p class="caption">Whakatane District- 15,700 footpath faults.<br>Individually located and prioritised.</p>

    <footer class="brand">
      <div class="brand-name"><span class="brand-dot"></span>Groundline Surveys Ltd</div>
      <div class="brand-web">www.groundlinesurveys.co.nz</div>
    </footer>
  </main>
</body>
</html>
```